Organic Herbs & Spices container

Greek startup company, which cultivate and trade spices and herbs (such as oregano, mint, thyme, sage etc.)

At present we are interested in only the type and shape of packaging which should be made by materials such as paper, cardboard, laminated paper and others based on paper or plastic.

Package size vary from 80g (2.82oz) - 300g (10.58oz). We are going to use the same packing for a variety of products with different information

* Please find attached our logo which should be included in the design.
* There is no company name available at the moment, however a name placeholder should be included.
* include a placeholder for the type of product (sage, oregano, mint, tea etc...).
* Each package should have a place in order to include product details and nutrition facts.

e.g.
xxxx (company name placeholder)
Sage (product type)
product details and nutrition facts.
Updates

Dear designers,first of all, thank you for your proposals. Please find bellow some updates for the project.- It is mandatory to include the logo into the design - Each package should be able to stored vertically - We are looking for one specific package design, please do not submit many variations of a certain package neither colour differentiations Thanks and good luck Added Wednesday, September 28, 2016

Please avoid the use of images. The same package will be used for all the kinds of products (only name and maybe colour will be different among different products. A transparent frame that will show the contents could be used too) Added Wednesday, September 28, 2016

Please find attached logo in EPS format

Our logo is the baseline, any concepts should be based on it. Try to avoid just adding the logo as a small sticker somewhere on the design. Please try to create around it at any way toy like. This could be, to visualize it as a 3D shape or object which can be used as the container of the products.

Reason: We would like to extend the time of the project. We believe that most of the submitted designs do not comply with our requirements.

Reason: We would like to see a bigger variety of ideas

Target Market(s)

Pretty much to anyone over 20 years old worldwide.

Industry/Entity Type

Nutrition

Requirements
Must have
• It should be attractive, easily recognized, simple yet innovative, durable, functional (easy to use) and easy to store.
Should not have
• Project must not include complex or obnoxious shapes and colours.

```html
<!DOCTYPE html>
<html lang="en">
<head>
<meta charset="utf-8">
<title>Organic Herbs &amp; Spices – Container Series</title>
<link rel="stylesheet" href="https://fonts.googleapis.com/css2?family=Pathway+Gothic+One&family=Open+Sans:wght@700&display=swap">
<style>
  :root {
    --canvas: #ffffff;
    --panel: #ffffff;
    --ink: #111111;
    --brand-green: #1f6e2c;
    --cork: #b9946a;
    --cork-edge: #9c7850;
    --glass: #f1f3f2;
    --glass-edge: #d9dcdb;
    --salt-base: #a9aaad;
    --salt-tone-a: #ece9c4;
    --salt-tone-b: #5f8798;
    --salt-fill: #e4e5e5;
    --oregano-base: #3c7a4f;
    --oregano-tone: #14301b;
    --oregano-fill: #7d7c4c;
    --mint-base: #3c7a4f;
    --mint-tone: #5fb85a;
    --mint-fill: #4f6a3f;
    --chamomile-base: #1d4a23;
    --chamomile-tone: #b08a2c;
    --chamomile-fill: #c6c4a2;
  }
  html, body {
    margin: 0;
    padding: 0;
    width: 1200px;
    height: 790px;
    overflow: hidden;
    background: var(--canvas);
  }
  .series {
    position: relative;
    width: 1200px;
    height: 790px;
  }

  /* container */
  .jar {
    position: absolute;
    top: 112px;
    width: 156px;
    height: 560px;
  }
  .jar--salt { left: 153px; }
  .jar--oregano { left: 405px; }
  .jar--mint { left: 656px; }
  .jar--chamomile { left: 906px; }

  .jar__cap {
    position: absolute;
    top: 0;
    left: 1px;
    width: 154px;
    height: 38px;
    border-radius: 4px 4px 2px 2px;
    background: var(--cork);
    border-bottom: 2px solid var(--cork-edge);
    box-sizing: border-box;
  }
  .jar__body {
    position: absolute;
    top: 36px;
    left: 0;
    width: 156px;
    height: 522px;
    box-sizing: border-box;
    background: var(--glass);
    border: 1px solid var(--glass-edge);
    border-radius: 0 0 14px 14px;
    overflow: hidden;
  }
  .jar__contents {
    position: absolute;
    left: 3px;
    right: 3px;
    top: 374px;
    bottom: 5px;
    border-radius: 0 0 11px 11px;
  }
  .jar--salt .jar__contents { background: var(--salt-fill); }
  .jar--oregano .jar__contents { background: linear-gradient(180deg, #6f7040, var(--oregano-fill)); }
  .jar--mint .jar__contents { background: linear-gradient(180deg, #3f5a32, var(--mint-fill)); }
  .jar--chamomile .jar__contents { background: linear-gradient(180deg, #b8b88e, var(--chamomile-fill)); }

  /* label wrap */
  .label {
    position: absolute;
    top: 10px;
    left: 1px;
    width: 152px;
    height: 364px;
    overflow: hidden;
  }
  .jar--salt .label { background: var(--salt-base); }
  .jar--oregano .label { background: var(--oregano-base); }
  .jar--mint .label { background: var(--mint-base); }
  .jar--chamomile .label { background: var(--chamomile-base); }

  .label__pattern {
    position: absolute;
    left: 0;
    right: 0;
    top: 140px;
    bottom: 0;
  }
  .jar--salt .label__pattern {
    background: linear-gradient(165deg, var(--salt-base) 0%, var(--salt-tone-a) 50%, var(--salt-tone-b) 130%);
  }
  .jar--oregano .label__pattern {
    background: linear-gradient(165deg, var(--oregano-base) 0%, var(--oregano-tone) 90%);
  }
  .jar--mint .label__pattern {
    background: linear-gradient(165deg, var(--mint-base) 0%, var(--mint-tone) 90%);
  }
  .jar--chamomile .label__pattern {
    background: linear-gradient(165deg, var(--chamomile-base) 10%, var(--chamomile-tone) 120%);
  }

  .label__panel {
    position: absolute;
    top: 2px;
    left: 26px;
    width: 98px;
    height: 220px;
    background: var(--panel);
  }
  .brand {
    position: absolute;
    top: 12px;
    left: 0;
    right: 0;
    text-align: center;
  }
  .brand__dot {
    display: block;
    width: 30px;
    height: 30px;
    margin: 0 auto 22px;
    border-radius: 50%;
    background: var(--brand-green);
  }
  .brand__name {
    display: block;
    font-family: "Open Sans", Arial, sans-serif;
    font-weight: 700;
    font-size: 9px;
    color: var(--brand-green);
    letter-spacing: 0.2px;
  }
  .product {
    position: absolute;
    left: 0;
    right: 0;
    margin: 0;
    text-align: center;
    font-family: "Pathway Gothic One", "Arial Narrow", sans-serif;
    font-weight: 400;
    color: var(--ink);
    line-height: 1;
    white-space: nowrap;
  }
  .product--large { font-size: 60px; top: 148px; letter-spacing: 2px; }
  .product--medium { font-size: 27px; top: 172px; letter-spacing: 1px; }
  .product--small { font-size: 21px; top: 183px; letter-spacing: 0.5px; }
</style>
</head>
<body>
<main class="series">

  <article class="jar jar--salt">
    <div class="jar__cap"></div>
    <div class="jar__body">
      <section class="label">
        <div class="label__pattern" role="img" aria-label="Brush-stroke pattern in grey, cream and slate blue"></div>
        <div class="label__panel">
          <div class="brand"><span class="brand__dot"></span><span class="brand__name">BRAND NAME</span></div>
          <h2 class="product product--large">SALT</h2>
        </div>
      </section>
      <div class="jar__contents" role="img" aria-label="Fine white salt seen through the clear tube"></div>
    </div>
  </article>

  <article class="jar jar--oregano">
    <div class="jar__cap"></div>
    <div class="jar__body">
      <section class="label">
        <div class="label__pattern" role="img" aria-label="Brush-stroke pattern in deep green tones"></div>
        <div class="label__panel">
          <div class="brand"><span class="brand__dot"></span><span class="brand__name">BRAND NAME</span></div>
          <h2 class="product product--medium">OREGANO</h2>
        </div>
      </section>
      <div class="jar__contents" role="img" aria-label="Dried oregano seen through the clear tube"></div>
    </div>
  </article>

  <article class="jar jar--mint">
    <div class="jar__cap"></div>
    <div class="jar__body">
      <section class="label">
        <div class="label__pattern" role="img" aria-label="Brush-stroke pattern in fresh light green tones"></div>
        <div class="label__panel">
          <div class="brand"><span class="brand__dot"></span><span class="brand__name">BRAND NAME</span></div>
          <h2 class="product product--large">MINT</h2>
        </div>
      </section>
      <div class="jar__contents" role="img" aria-label="Dried mint leaves seen through the clear tube"></div>
    </div>
  </article>

  <article class="jar jar--chamomile">
    <div class="jar__cap"></div>
    <div class="jar__body">
      <section class="label">
        <div class="label__pattern" role="img" aria-label="Brush-stroke pattern in dark green and golden ochre"></div>
        <div class="label__panel">
          <div class="brand"><span class="brand__dot"></span><span class="brand__name">BRAND NAME</span></div>
          <h2 class="product product--small">CHAMOMILE</h2>
        </div>
      </section>
      <div class="jar__contents" role="img" aria-label="Dried chamomile flowers seen through the clear tube"></div>
    </div>
  </article>

</main>
</body>
</html>
```